Stonefield Partners Business Card Design

We are looking for a new business card design, we are not happy with our current design. We are a boutique management consulting firm and our clients are typically fortune 500 companies.

I have attached the current front and back that we have as well as a version of our logo that can be used. I am trying to get a higher resolution version of the logo file to upload to the project.

Target Market(s)

Fortune 500 companies are our primary client base. Financial services, life sciences, pharmaceuticals and telecom companies are

Industry/Entity Type

Management Consulting

Contact Information for Business Card

We are trying to communicate a high degree of professionalism, a somewhat minimalist perhaps with some air of whimsy (without overdoing it). Attached is the current design, front and back as well as logos. I like the current back of the card and assume we will keep the phrase the same.

From a color palette perspective, I prefer to stay with a gray scale as they are today.

Font styles to use
Sans Serif

Colors
1b1b1b
474747
ffffff

Requirements
Must have
• Two sided business card design. File format should be something that can be used outside of Photoshop like MS Publisher so that they can be edited with personal information.
• Font should be calibri or something very similar and should be available within MS Office
Should not have
• No other logos or graphics outside of the logo provided.

```html
<!DOCTYPE html>
<html lang="en">
<head>
<meta charset="utf-8">
<title>Stonefield Partners – Business Card</title>
<link href="https://fonts.googleapis.com/css2?family=Carlito:wght@400;700&display=swap" rel="stylesheet">
<style>
  :root {
    --stage: #000000;
    --card-light: #f3f3f3;
    --card-dark: #474747;
    --ink: #1b1b1b;
    --paper: #ffffff;
  }
  * { margin: 0; padding: 0; box-sizing: border-box; }
  html, body {
    width: 1200px; height: 900px; overflow: hidden;
    background: var(--stage);
    font-family: "Carlito", "Calibri", sans-serif;
  }
  .stage { position: relative; width: 1200px; height: 900px; }
  .card { position: absolute; top: 200px; height: 501px; }
  .card-front { left: 265px; width: 310px; background: var(--card-light); color: var(--ink); }
  .card-back { left: 641px; width: 308px; background: var(--card-dark); color: var(--paper); text-align: center; }

  .brand {
    position: absolute; left: 20px; top: 46px;
    display: flex; align-items: center; gap: 10px;
  }
  .brand-dot { width: 30px; height: 30px; border-radius: 50%; background: var(--ink); }
  .brand-name { font-weight: 700; font-size: 46px; line-height: 1; color: var(--ink); letter-spacing: -0.5px; }

  .contact { position: absolute; left: 29px; top: 269px; font-size: 14.5px; line-height: 18px; }
  .person-name { font-weight: 700; font-size: 19px; line-height: 24px; }
  .firm-block { margin-top: 22px; }
  .firm-name { font-weight: 700; }
  .reach { margin-top: 10px; list-style: none; }
  .reach li { display: flex; align-items: center; gap: 8px; line-height: 21px; }
  .reach svg { width: 10px; height: 10px; fill: var(--ink); flex: none; }

  .tagline {
    position: absolute; left: 0; right: 0; top: 46px;
    font-weight: 700; font-size: 27px; line-height: 35px;
  }
  .emblem {
    position: absolute; left: 0; right: 0; top: 275px;
    display: flex; justify-content: center; align-items: center; gap: 12px;
  }
  .emblem-dot { width: 38px; height: 38px; border-radius: 50%; background: var(--paper); }
  .emblem-name { font-weight: 700; font-size: 40px; line-height: 1; color: var(--paper); }
  .web { position: absolute; left: 0; right: 0; top: 452px; font-weight: 700; font-size: 14.5px; }
</style>
</head>
<body>
<main class="stage">
  <section class="card card-front">
    <div class="brand">
      <span class="brand-dot"></span>
      <span class="brand-name">Stonefield</span>
    </div>
    <div class="contact">
      <p class="person-name">Mark Ellison</p>
      <p>Los Angeles Office</p>
      <p>Managing Director</p>
      <div class="firm-block">
        <p class="firm-name">Stonefield Partners, Inc</p>
        <p>Headquarters 218</p>
        <p>Harbor View Road Suite 204</p>
        <p>Lakewood, WA 98499</p>
      </div>
      <ul class="reach">
        <li>
          <svg viewBox="0 0 10 10" aria-hidden="true"><path d="M2 0.5l1.6 2.2-1 1a6 6 0 0 0 3.7 3.7l1-1L9.5 8 8.3 9.5C4 9.3 0.7 6 0.5 1.7z"/></svg>
          <span>206.555.0147</span>
        </li>
        <li>
          <svg viewBox="0 0 10 10" aria-hidden="true"><path d="M0.5 2h9v6h-9z M0.5 2.4l4.5 3.2 4.5-3.2" fill="var(--ink)" stroke="var(--card-light)" stroke-width="0.8"/></svg>
          <span>mellison@stonefieldpartners.com</span>
        </li>
      </ul>
    </div>
  </section>

  <section class="card card-back">
    <h1 class="tagline">The preferred choice<br>for leadership's top<br>priorities</h1>
    <div class="emblem">
      <span class="emblem-dot"></span>
      <span class="emblem-name">Stonefield</span>
    </div>
    <p class="web">www.StonefieldPartners.com</p>
  </section>
</main>
</body>
</html>
```